PowerPoint template for large technology company

Requesting proposals for a PowerPoint deck template that can be used by our sales team when pitching clients. We are a large technology media company, that is BtoB focused, and are looking for a professional, clean, tech-forward, design and layout. However, our clients are advertisers and brands who would respond well to a subtly stylized creative design.

We need a fully built-out template wherein our sales team can choose from a variety of slide layouts while compiling their pitch decks.

Key objective: To create a template that mandates consistent fonts, sizes, and layout, and is easy to use for novice presenters. A plug-and-play template.

Secondary objective: A refresh on current design of company template.

Presentation template should include:
2 Presentation title slide options
2 Section header options
6 information layout slide options
3 data charts (pie, bar, and column)
Summary/ Thank you slide

The teams using this template will not be adept with PowerPoint but should easily be able to insert images and text boxes without it ruining the design and format of the presentation. The idea is if 20 people use our template to build pitch-decks, all of the individual decks should all look like they came from the same team. Please be as detailed and specific as possible when building out slides.

Simple, high-compatibility fonts. Please see brand guidelines attached.

Target Market(s)

Large advertising agencies and major consumer technology brands.

This deck template will not be consumer facing.

Industry/Entity Type

Building

Font styles to use
Serif
Sans Serif

Requirements
Must have
• Must be clean, high-tech, and forces user to stay within template guidelines during modifications.

Template should be built out for a sales presentation that will be a tool for ppt novices.
Nice to have
• As we are revamping existing decks, it will be nice to see multiple ideas on the design. Think professional, high-tech, and powerful.
Should not have
• Should not have a distracting background that will interfere with presentations or where it will be difficult to easily insert images.

Blacked out backgrounds cause a "boxed in" look for images and/or text boxes - which is undesirable. Either don't include color-blocked backgrounds or introduce a way in which this can be used that avoids the previously stated pitfall.

No rotated text-fill options. (i.e. rotating text by 90 or 180 degrees)

Please don't be too literal in your design approach.

```html
<!DOCTYPE html>
<html lang="en">
<head>
<meta charset="utf-8">
<title>Corestream Presentation Template</title>
<link rel="stylesheet" href="https://fonts.googleapis.com/css2?family=Libre+Baskerville:wght@400;700&family=Roboto:wght@300;400&display=swap">
<style>
:root{
  --stage:#232323;
  --slide-light:#f4f5f6;
  --slide-mid:#e3e5e8;
  --brand-blue:#0f5f9a;
  --ink:#2b2b2b;
  --ink-soft:#6a6f75;
  --body:#5d6166;
  --marker:#8a949e;
  --rule:#4a4a4a;
  --white:#ffffff;
  --muted:#8d8d8d;
}
*{margin:0;padding:0;box-sizing:border-box}
html,body{width:1200px;height:1200px;overflow:hidden;background:var(--stage)}
.board{position:relative;width:1200px;height:1200px;font-family:'Roboto',Arial,sans-serif}
.slide{position:absolute;left:238px;width:724px;height:452px;overflow:hidden;
  background:radial-gradient(ellipse at 45% 35%,var(--slide-light) 0%,var(--slide-mid) 100%)}
.slide--products{top:58px}
.slide--portfolio{top:570px}
.abs{position:absolute}
.wordmark{font-family:'Roboto',Arial,sans-serif;font-weight:400;color:#3d4550;line-height:1}
.tagline{font-size:6.5px;color:#3d4550;line-height:1}
.serif{font-family:'Libre Baskerville',Georgia,serif;font-weight:700}

/* slide 1 */
.slide--products .wordmark{left:62px;top:22px;font-size:17px}
.slide--products .tagline{left:94px;top:41px}
.header-divider{left:174px;top:14px;width:2px;height:44px;background:linear-gradient(#fff0,#c9ccd0,#fff0)}
.slide--products .headline{left:190px;top:18px;font-size:13.5px;color:var(--brand-blue)}
.slide--products .category-label{left:190px;top:37px;font-size:10px;color:var(--ink-soft)}
.page-tag{left:619px;top:8px}
.page-tag span{position:absolute;font-family:'Libre Baskerville',Georgia,serif;font-size:7px;color:var(--ink-soft);top:16px;left:0}
.page-tag svg{position:absolute;left:19px;top:0}
.page-tag b{position:absolute;left:24px;top:10px;font-size:10px;color:var(--white);font-weight:400;font-family:'Libre Baskerville',Georgia,serif}
.device-visual{left:66px;top:126px;width:266px;height:194px;border-radius:6px;
  background:linear-gradient(135deg,#2a2a2a 0%,#3a3a3a 55%,#cfd2d5 56%,#c4c7ca 100%)}
.backdrop-shape{left:0;top:240px}
.category{position:absolute;width:130px}
.category h3{font-family:'Libre Baskerville',Georgia,serif;font-weight:700;font-size:10px;color:var(--ink);
  position:absolute;left:25px;top:0}
.category svg{position:absolute;left:0;top:-6px}
.category p{position:absolute;top:24px;left:0;font-size:7.3px;line-height:13.6px;color:var(--body);width:130px}

/* slide 2 */
.slide--portfolio{background:radial-gradient(ellipse at 40% 40%,#f5f6f7 0%,#e2e4e6 100%)}
.slide--portfolio .headline{left:49px;top:16px;font-size:19px;color:var(--ink)}
.slide--portfolio .subtitle{left:49px;top:38px;font-size:12.5px;color:var(--ink-soft);font-weight:300}
.page-badge{left:645px;top:6px}
.page-badge span{position:absolute;left:0;top:14px;font-size:10px;color:var(--muted);font-weight:300}
.page-badge i{position:absolute;left:27px;top:0;width:33px;height:33px;border-radius:50%;background:var(--brand-blue);
  color:var(--white);font-style:normal;font-size:18px;font-weight:300;text-align:center;line-height:33px}
.item{position:absolute;width:260px}
.item::before{content:"";position:absolute;left:0;top:3px;width:11px;height:11px;background:var(--marker)}
.item h3{position:absolute;left:24px;top:0;font-family:'Libre Baskerville',Georgia,serif;font-weight:700;font-size:13.5px;color:var(--ink);white-space:nowrap}
.item p{position:absolute;left:24px;top:22px;width:262px;font-size:7.6px;line-height:13.6px;color:var(--body);font-weight:300}
.footer-band{height:5px;background:var(--brand-blue);top:427px;border-bottom:2px solid #cfd5dc}
.footer-band--left{left:0;width:38px}
.footer-band--right{left:160px;width:564px}
.slide--portfolio .wordmark{left:51px;top:420px;font-size:17px}
.slide--portfolio .tagline{left:81px;top:439px}

/* presentation footer */
.stage-rule{left:38px;top:1067px;width:1108px;height:1px;background:var(--rule)}
.stage-wordmark{left:98px;top:1118px;font-size:38px;color:var(--white);font-weight:300;line-height:1}
.stage-tagline{left:160px;top:1156px;font-size:12px;color:var(--white)}
.stage-caption{left:728px;top:1113px;font-size:19px;color:var(--white);letter-spacing:.2px}
</style>
</head>
<body>
<main class="board">

  <section class="slide slide--products">
    <svg class="abs backdrop-shape" width="260" height="220" viewBox="0 0 260 220" aria-hidden="true">
      <polygon points="0,0 210,110 0,220" fill="#d9dce0" opacity=".45"/>
    </svg>
    <div class="abs wordmark">Corestream</div>
    <div class="abs tagline">Insight Driven Media</div>
    <div class="abs header-divider"></div>
    <h1 class="abs serif headline">Headline Title Goes Here</h1>
    <div class="abs category-label">Product Category</div>
    <div class="abs page-tag">
      <span>Page</span>
      <svg width="28" height="33" viewBox="0 0 28 33"><polygon points="0,0 28,16.5 0,33" fill="var(--brand-blue)"/></svg>
      <b>2</b>
    </div>
    <div class="abs device-visual" role="img" aria-label="Desktop monitor showing the title slide of the presentation"></div>

    <div class="category" style="left:382px;top:135px">
      <svg width="22" height="20" viewBox="0 0 22 20"><rect x="0" y="0" width="5" height="20" fill="#9aa2a9"/><polygon points="5,0 22,10 5,20" fill="var(--brand-blue)"/></svg>
      <h3>Category 1</h3>
      <p>This is just dummy text. You can replace this with real content. Collaboratively administrate empowered markets via plug-and-play networks.</p>
    </div>
    <div class="category" style="left:522px;top:135px">
      <svg width="22" height="20" viewBox="0 0 22 20"><rect x="0" y="0" width="5" height="20" fill="#9aa2a9"/><polygon points="5,0 22,10 5,20" fill="var(--brand-blue)"/></svg>
      <h3>Category 2</h3>
      <p>This is just dummy text. You can replace this with real content. Collaboratively administrate empowered markets via plug-and-play networks.</p>
    </div>
    <div class="category" style="left:382px;top:261px">
      <svg width="22" height="20" viewBox="0 0 22 20"><rect x="0" y="0" width="5" height="20" fill="#9aa2a9"/><polygon points="5,0 22,10 5,20" fill="var(--brand-blue)"/></svg>
      <h3>Category 3</h3>
      <p>This is just dummy text. You can replace this with real content. Collaboratively administrate empowered markets via plug-and-play networks.</p>
    </div>
    <div class="category" style="left:522px;top:261px">
      <svg width="22" height="20" viewBox="0 0 22 20"><rect x="0" y="0" width="5" height="20" fill="#9aa2a9"/><polygon points="5,0 22,10 5,20" fill="var(--brand-blue)"/></svg>
      <h3>Category 4</h3>
      <p>This is just dummy text. You can replace this with real content. Collaboratively administrate empowered markets via plug-and-play networks.</p>
    </div>
  </section>

  <section class="slide slide--portfolio">
    <h1 class="abs serif headline">Headline Title Goes Here</h1>
    <div class="abs subtitle">Subtitle Write Here</div>
    <div class="abs page-badge"><span>PAGE</span><i>04</i></div>

    <div class="item" style="left:62px;top:113px">
      <h3>Desk One</h3>
      <p>Efficiently unleash cross-media information without cross-media value. Quickly maximize timely deliverables for real-time schemas. Dramatically maintain clicks-and-mortar solutions without functional solutions.</p>
    </div>
    <div class="item" style="left:379px;top:113px">
      <h3>Mini Desk</h3>
      <p>Efficiently unleash cross-media information without cross-media value. Quickly maximize timely deliverables for real-time schemas. Dramatically maintain clicks-and-mortar solutions without functional solutions.</p>
    </div>
    <div class="item" style="left:62px;top:206px">
      <h3>Axelon</h3>
      <p>Professionally cultivate one-to-one customer service with robust ideas. Dynamically innovate resource-leveling customer service for state of the art customer service.</p>
    </div>
    <div class="item" style="left:379px;top:206px">
      <h3>Orbit TV</h3>
      <p>Professionally cultivate one-to-one customer service with robust ideas. Dynamically innovate resource-leveling customer service for state of the art customer service.</p>
    </div>
    <div class="item" style="left:62px;top:297px">
      <h3>Brightline Mobile</h3>
      <p>Efficiently unleash cross-media information without cross-media value. Quickly maximize timely deliverables for real-time schemas. Dynamically procrastinate B2C users after installed base benefits.</p>
    </div>
    <div class="item" style="left:379px;top:297px">
      <h3>Slate Pad</h3>
      <p>Efficiently unleash cross-media information without cross-media value. Quickly maximize timely deliverables for real-time schemas. Dynamically procrastinate B2C users after installed base benefits.</p>
    </div>

    <div class="abs footer-band footer-band--left"></div>
    <div class="abs footer-band footer-band--right"></div>
    <div class="abs wordmark">Corestream</div>
    <div class="abs tagline">Insight Driven Media</div>
  </section>

  <div class="abs stage-rule"></div>
  <div class="abs stage-wordmark">Corestream</div>
  <div class="abs stage-tagline">Insight Driven Media</div>
  <div class="abs stage-caption">POWER POINT PRESENTATION</div>

</main>
</body>
</html>
```